Web Page Design for a Website that Provides Tutoring

I am looking to create an online tutoring website. The website will allow parents or students to contact tutors with a view to instructing them to tutor themselves or their children.

The name of the website is LendYourLessons.

This brief is to create the design for one of the web pages for this web site. I am hoping the same designer will be available to design other pages.

The page I want designed is one of the more complex and I have attached the design as an excel spreadsheet. The web page needs to include all the items on this page but if you want to change the positioning of the items then Im fine with that.

I recently had two logos created for this website. My favourite is the one with a mortar board but im not sure I like the colours. I have attached both of these logos and you can use either of them, change the colours or create something different. I just want a design pleasing to the eye. If the logo is changed I would like that in a seperate file.

So can you please submit designs for this page. I have attached the two logos which you can use, change or if you feel you have a better idea then you can use that.

On the spreadsheet the Send Message, Favourite etc are buttons.

Target Market(s)

People who want to better themselves.
Possible middle class to upper class.

Industry/Entity Type

Tutoring

Number of Pages Required

1 page

Requirements
Must have
• The designs must have alot of the information attached in the spreadsheet.

```html
<!DOCTYPE html>
<html lang="en">
<head>
<meta charset="utf-8">
<title>LendYourLessons – Tutor Profile</title>
<link href="https://fonts.googleapis.com/css2?family=Roboto:wght@300;400;500;700&display=swap" rel="stylesheet">
<style>
:root{
  --orange:#f5921e;
  --coral:#fb6341;
  --navy:#2f5590;
  --blue:#3e68b0;
  --dark:#24272c;
  --text:#2b2b2b;
  --muted:#555;
  --line:#d6d6d6;
  --pale:#eef1fb;
  --green:#d9fbd5;
  --star:#fb6341;
  --star-off:#c9c9c9;
}
*{box-sizing:border-box;margin:0;padding:0}
html,body{width:810px;height:1200px;overflow:hidden}
body{font-family:'Roboto',sans-serif;color:var(--text);background:#fff;position:relative;font-size:8px}
.abs{position:absolute}
/* header */
.site-header{position:absolute;left:0;top:0;width:810px;height:62px;background:#fff}
.brand{position:absolute;left:54px;top:20px;display:flex;align-items:center;gap:5px;font-size:20px;font-weight:500;color:var(--orange)}
.brand-mark{width:10px;height:10px;background:var(--navy)}
.main-nav{position:absolute;top:27px;font-size:9.5px;color:#222}
.main-nav span{position:absolute;white-space:nowrap}
.main-nav .active{color:var(--navy);border-bottom:1px solid var(--navy);padding-bottom:2px}
.btn{position:absolute;display:flex;align-items:center;justify-content:center;font-weight:500;color:#fff;font-size:9px}
.btn-login{left:624px;top:19px;width:62px;height:26px;background:var(--orange)}
.btn-register{left:693px;top:19px;width:62px;height:26px;background:var(--coral)}
.crumb-bar{position:absolute;left:0;top:62px;width:810px;height:39px;background:var(--dark)}
.crumbs{position:absolute;left:54px;top:11px;font-size:12px;font-weight:300;color:#c9c9c9}
.btn-favour{left:692px;top:11px;width:61px;height:19px;border:1px solid var(--coral);color:var(--coral);font-size:7px}
/* panels */
.panel{position:absolute;border:1px solid var(--line);background:#fff}
.panel-head{height:22px;background:var(--orange);color:#fff;font-size:10.5px;font-weight:500;padding:5px 7px;margin:-1px -1px 0}
.panel-head.coral{background:var(--coral)}
.stars{display:flex;gap:2px}
.stars svg{width:12px;height:12px}
/* profile */
.profile{left:54px;top:122px;width:462px;height:146px}
.profile-name{position:absolute;left:9px;top:8px;font-size:13px}
.photo{position:absolute;left:10px;top:28px;width:98px;height:106px;background:linear-gradient(160deg,#6d6a66,#2e2d2c)}
.facts{position:absolute;left:116px;top:29px;line-height:16px;font-size:8px;color:#444}
.facts b{font-weight:500;color:#222}
.badge{position:absolute;left:116px;top:114px;width:22px;height:18px;border:2px solid #e0408d;border-radius:4px}
.location{position:absolute;left:288px;top:0;width:173px;height:144px;background:var(--pale);padding:7px 13px}
.location h3{font-size:13px;font-weight:400}
.location .miles{font-size:8.5px;font-weight:500;margin-top:4px}
.location .label{font-size:8px;font-weight:500;margin-top:16px}
.loc-list{margin:6px 0 0 8px;font-size:8px;line-height:15.5px}
.loc-list div{display:flex;justify-content:space-between;width:78px}
.location .travel{font-size:8px;margin-top:6px}
/* scoring */
.scoring{left:534px;top:122px;width:221px;height:146px}
.score-row{position:absolute;left:11px;display:flex;align-items:center;font-size:8px;font-weight:500}
.score-row span{width:82px}
/* tutor info */
.info{left:54px;top:286px;width:462px;height:146px}
.info-body{padding:10px 16px 0 17px;font-size:8px;line-height:13.3px;color:#333;height:115px;overflow:hidden}
.info-body p+p{margin-top:8px}
.scrollmark{position:absolute;right:4px;width:2px;height:14px;background:var(--coral)}
/* history */
.history{left:54px;top:446px;width:462px;height:103px}
.hist-col{position:absolute;top:34px;font-size:8px}
.hist-col h4{font-size:8px;font-weight:500;margin-bottom:13px}
.hist-col .row span{display:inline-block}
.divider{position:absolute;top:34px;width:2px;height:62px;background:#ccc}
/* subjects */
.subjects{left:54px;top:562px;width:462px;height:140px}
.subjects table{width:100%;border-collapse:collapse;font-size:9px}
.subjects th{background:#d9d9d9;font-weight:400;font-size:8px;color:#444;height:24px;text-align:left}
.subjects td{height:20.5px;border-bottom:1px solid #ddd}
.subjects tr:last-child td{border-bottom:none}
.subjects td:first-child,.subjects th:first-child{padding-left:10px}
.subjects tbody tr:first-child td{padding-top:6px;height:26px}
/* availability */
.avail{left:54px;top:720px;width:462px;height:158px}
.avail .panel-head{display:flex;justify-content:space-between}
.month{display:flex;align-items:center;gap:8px;font-size:8px;font-weight:400}
.days{position:absolute;left:0;top:24px;width:460px;height:24px;background:#d9d9d9;font-size:8px;color:#333}
.days span{position:absolute;top:7px}
.grid{position:absolute;left:67px;top:55px;width:384px;height:62px;background:var(--green)}
.slot-label{position:absolute;left:10px;font-size:8.5px}
.bar{position:absolute;height:7px}
.taken{background:var(--coral)}.reserved{background:var(--orange)}.no{background:var(--navy)}
.legend{position:absolute;left:108px;top:129px;display:flex;gap:9px;font-size:8px;color:#555}
.legend i{display:inline-block;width:6px;height:6px;margin-right:3px;vertical-align:0}
/* contact */
.contact{left:534px;top:286px;width:221px;height:194px;background:var(--pale)}
.field{position:absolute;left:11px;width:198px;background:#fff;border:1px solid #ccc;color:#888;font-size:8.5px;padding:8px 8px}
.btn-submit{left:148px;top:154px;width:61px;height:22px;background:var(--navy);font-size:9px}
/* reviews */
.reviews{left:534px;top:499px;width:221px;height:379px;background:var(--pale)}
.review{position:absolute;left:12px;width:198px;height:122px;border:1px solid #ccc;background:var(--pale)}
.avatar{position:absolute;left:11px;top:10px;width:40px;height:38px}
.review .stars{position:absolute;left:60px;top:34px}
.review p{position:absolute;left:12px;top:56px;width:176px;font-size:8px;line-height:11px;color:#333}
.review .who{position:absolute;left:18px;top:103px;font-size:8px}
.btn-place{left:39px;top:306px;width:142px;height:20px;background:var(--navy);font-size:9px}
.btn-all{left:39px;top:336px;width:142px;height:20px;border:1px solid var(--coral);color:var(--coral);font-size:9px;background:#fff}
/* footer */
.site-footer{position:absolute;left:0;top:909px;width:810px;height:256px;background:linear-gradient(180deg,#4470b6,#3a64ac)}
.foot-head{position:absolute;top:50px;font-size:15px;font-weight:300;color:var(--orange)}
.foot-rule{position:absolute;top:65px;height:1px;background:rgba(255,255,255,.5)}
.foot-links{position:absolute;top:76px;font-size:9px;color:#fff;line-height:18px}
.foot-links div::before{content:"";display:inline-block;border-left:3px solid #fff;border-top:2.5px solid transparent;border-bottom:2.5px solid transparent;margin-right:5px;vertical-align:1px}
.contact-info{position:absolute;left:268px;top:77px;color:#fff;font-size:8px;line-height:10.5px}
.contact-info .row{display:flex;gap:7px;margin-bottom:8px}
.contact-info .phone{font-size:11px;color:var(--orange);font-weight:400}
.map{position:absolute;left:474px;top:76px;width:111px;height:85px;border:3px solid #b4c3de;background:linear-gradient(135deg,#e7e2d2,#d9d2b6)}
.social{position:absolute;left:630px;top:78px;font-size:8.5px;color:#fff;line-height:22.7px}
.social div{display:flex;align-items:center;gap:8px}
.social i{display:inline-block;width:16px;height:16px;background:#fff;opacity:.85}
.copy-bar{position:absolute;left:0;top:1165px;width:810px;height:35px;background:var(--orange);color:#fff;font-size:7.5px}
.copy-bar .left{position:absolute;left:51px;top:13px}
.copy-bar .right{position:absolute;right:30px;top:13px}
</style>
</head>
<body>
<svg width="0" height="0" style="position:absolute">
  <symbol id="star" viewBox="0 0 24 24"><path d="M12 1.5l3.2 7 7.6.8-5.7 5.1 1.6 7.5L12 18l-6.7 3.9 1.6-7.5L1.2 9.3l7.6-.8z"/></symbol>
</svg>

<header class="site-header">
  <div class="brand"><span class="brand-mark"></span>LendYourLessons</div>
  <nav class="main-nav">
    <span style="left:322px">Home</span>
    <span style="left:370px" class="active">Search</span>
    <span style="left:422px">Student</span>
    <span style="left:479px">Tutor</span>
    <span style="left:527px">About</span>
    <span style="left:577px">Contact</span>
  </nav>
  <a class="btn btn-login">Login</a>
  <a class="btn btn-register">Register</a>
</header>

<div class="crumb-bar">
  <div class="crumbs">Home &gt; Search &gt; Teacher Name</div>
  <a class="btn btn-favour">FAVOUR</a>
</div>

<section class="panel profile">
  <div class="profile-name">Oliver Pembridge</div>
  <div class="photo" role="img" aria-label="Portrait photo of the tutor"></div>
  <div class="facts">
    <div><b>Age Group :</b> 35-40</div>
    <div><b>Gender:</b> Male</div>
    <div><b>Member Since :</b> 12th Jan 2014</div>
    <div><b>Avg Response Time :</b> 6pm to 10:30pm</div>
    <div><b>Member Since &nbsp;:</b> 26th Dec, 2016</div>
  </div>
  <div class="badge"></div>
  <div class="location">
    <h3>Ashcombe Vale</h3>
    <div class="miles">3.51Miles way</div>
    <div class="label">Tution Loction :</div>
    <div class="loc-list">
      <div>Tutors Home <svg width="9" height="8" viewBox="0 0 10 8"><path d="M1 4l3 3 5-6" stroke="#3aa64a" stroke-width="1.4" fill="none"/></svg></div>
      <div>Online <svg width="9" height="8" viewBox="0 0 10 8"><path d="M1 4l3 3 5-6" stroke="#3aa64a" stroke-width="1.4" fill="none"/></svg></div>
      <div>Travel to Student <svg width="9" height="9" viewBox="0 0 10 10"><path d="M1 1l8 8M9 1l-8 8" stroke="#e23b2e" stroke-width="1.4"/></svg></div>
    </div>
    <div class="travel"><b style="font-weight:500">Miles able to travel :</b> N/A</div>
  </div>
</section>

<section class="panel scoring">
  <div class="panel-head coral">Scoring</div>
  <div class="score-row" style="top:38px"><span>Reviews :</span><div class="stars" style="fill:var(--star)"><svg><use href="#star"/></svg><svg><use href="#star"/></svg><svg><use href="#star"/></svg><svg><use href="#star"/></svg><svg><use href="#star"/></svg></div></div>
  <div class="score-row" style="top:74px"><span>Reliability :</span><div class="stars"><svg fill="var(--star)"><use href="#star"/></svg><svg fill="var(--star)"><use href="#star"/></svg><svg fill="var(--star)"><use href="#star"/></svg><svg fill="var(--star)"><use href="#star"/></svg><svg fill="var(--star-off)"><use href="#star"/></svg></div></div>
  <div class="score-row" style="top:110px"><span>Knowledge Center:</span><div class="stars" style="fill:var(--star)"><svg><use href="#star"/></svg><svg><use href="#star"/></svg><svg><use href="#star"/></svg><svg><use href="#star"/></svg><svg><use href="#star"/></svg></div></div>
</section>

<section class="panel info">
  <div class="panel-head">Tutor Informtion</div>
  <span class="scrollmark" style="top:32px"></span>
  <div class="info-body">
    <p>Hello,</p>
    <p>My name is Daniel Harlow, and I am a Historian specialized in languages and Ancient History. I am from Valmora but I studied in different places of Esteria. I have a Bachelor Degree in History from the University of Carvallo. This degree is structured in a significant freedom of subjects choice (three years studying universal, general and heoretical History and two years studying Ancient History, Art, Languages and Beliefs).<br>Besides, I started an Undergraduate Degree in Classical Studies from Valmora Open University. This degree provides you a strong background about language studies, the roots of European languages, a comparative study of</p>
  </div>
</section>

<section class="panel history">
  <div class="panel-head">History</div>
  <div class="hist-col" style="left:14px"><h4>Qualifications</h4><div class="row"><span style="width:57px">June 97</span><span style="width:104px">University of Westmere</span><span>2nd</span></div></div>
  <div class="divider" style="left:226px"></div>
  <div class="hist-col" style="left:237px"><h4>Work Experience</h4><div class="row"><span style="width:101px">Apr- 06 to Present</span><span>Halden &amp; Crane</span></div></div>
  <div class="divider" style="left:456px;background:#ccc"></div>
  <span class="scrollmark" style="top:34px;right:5px"></span>
</section>

<section class="panel subjects">
  <div class="panel-head">Subjects Taught</div>
  <table>
    <colgroup><col style="width:84px"><col style="width:49px"><col style="width:61px"><col style="width:46px"><col style="width:56px"><col style="width:68px"><col></colgroup>
    <thead><tr><th></th><th>Primary</th><th>Secondary</th><th>GCSE</th><th>A-LEVEL</th><th>University</th><th>Adult Learner</th></tr></thead>
    <tbody>
      <tr><td>Biology</td><td>£20</td><td>£20</td><td>£20</td><td></td><td>£20</td><td>£20</td></tr>
      <tr><td>Chemistry</td><td>£20</td><td>£20</td><td>£20</td><td></td><td>£20</td><td>£20</td></tr>
      <tr><td>Life Science</td><td>£20</td><td>£20</td><td>£20</td><td></td><td>£20</td><td>£20</td></tr>
      <tr><td>English</td><td>£20</td><td>£20</td><td>£20</td><td></td><td>£20</td><td>£20</td></tr>
    </tbody>
  </table>
</section>

<section class="panel avail">
  <div class="panel-head"><span>Availability</span>
    <span class="month">December 2016
      <svg width="6" height="9" viewBox="0 0 6 10"><path d="M5 1L1 5l4 4" stroke="#fff" fill="none" stroke-width="1.3"/></svg>
      <svg width="14" height="13" viewBox="0 0 14 13"><rect x="1" y="2" width="12" height="10" fill="none" stroke="#fff"/><path d="M1 5h12M4 0v3M10 0v3M4 7h1M7 7h1M10 7h1M4 9.5h1M7 9.5h1M10 9.5h1" stroke="#fff"/></svg>
      <svg width="6" height="9" viewBox="0 0 6 10"><path d="M1 1l4 4-4 4" stroke="#fff" fill="none" stroke-width="1.3"/></svg>
    </span>
  </div>
  <div class="days">
    <span style="left:68px">Mon (7th)</span><span style="left:116px">Tues (8th)</span><span style="left:164px">Wednes (9th)</span><span style="left:224px">Thurs (10th)</span><span style="left:292px">Fri (11th)</span><span style="left:345px">Satur (12th)</span><span style="left:406px">Sun(13th)</span>
  </div>
  <div class="grid"></div>
  <span class="slot-label" style="top:59px">7-8PM</span>
  <span class="slot-label" style="top:82px">8-9PM</span>
  <span class="slot-label" style="top:105px">4-5PM</span>
  <span class="bar taken" style="left:165px;top:64px;width:35px"></span>
  <span class="bar reserved" style="left:165px;top:81px;width:35px"></span>
  <span class="bar no" style="left:165px;top:99px;width:35px"></span>
  <span class="bar reserved" style="left:293px;top:99px;width:35px"></span>
  <span class="bar no" style="left:406px;top:75px;width:36px"></span>
  <div class="legend"><span><i style="background:var(--green)"></i>Available</span><span><i class="taken"></i>Taken</span><span><i class="reserved"></i>Reserved</span><span><i class="no"></i>No</span></div>
</section>

<section class="panel contact">
  <div class="panel-head coral">Contact Daniel Harlow</div>
  <div class="field" style="top:39px;height:26px">Subject</div>
  <div class="field" style="top:76px;height:68px">Enter your messages</div>
  <a class="btn btn-submit">SUBMIT</a>
</section>

<section class="panel reviews">
  <div class="panel-head coral">Tutors Review</div>
  <article class="review" style="top:37px">
    <div class="avatar" role="img" aria-label="Reviewer profile photo" style="background:linear-gradient(160deg,#c9b7a6,#6b5646)"></div>
    <div class="stars"><svg fill="var(--star)"><use href="#star"/></svg><svg fill="var(--star)"><use href="#star"/></svg><svg fill="var(--star)"><use href="#star"/></svg><svg fill="var(--star)"><use href="#star"/></svg><svg fill="var(--star-off)"><use href="#star"/></svg></div>
    <p>“Lorem ipsum dolor sit amet, consectetur adipiscing elit. Donec et quam nunc. Nam tortor sapien, volutpat consectetur lacus ut, accumsan viverra urna. ”</p>
    <div class="who">- Student Name</div>
  </article>
  <article class="review" style="top:171px">
    <div class="avatar" role="img" aria-label="Reviewer profile photo" style="background:linear-gradient(160deg,#cfb49a,#7a5a45)"></div>
    <div class="stars"><svg fill="var(--star)"><use href="#star"/></svg><svg fill="var(--star)"><use href="#star"/></svg><svg fill="var(--star)"><use href="#star"/></svg><svg fill="var(--star-off)"><use href="#star"/></svg><svg fill="var(--star-off)"><use href="#star"/></svg></div>
    <p>“Lorem ipsum dolor sit amet, consectetur adipiscing elit. Donec et quam nunc. Nam tortor sapien, volutpat consectetur lacus ut, accumsan viverra urna. ”</p>
    <div class="who">- Student Name</div>
  </article>
  <a class="btn btn-place">PLACE A REVIEW</a>
  <a class="btn btn-all">TO SEE ALL REVIEWS</a>
</section>

<footer class="site-footer">
  <div class="foot-head" style="left:54px">Quick Links</div>
  <div class="foot-rule" style="left:54px;width:180px"></div>
  <div class="foot-links" style="left:57px"><div>Home</div><div>About</div><div>Search</div><div>Student</div><div>Tutor</div><div>Contacts</div></div>
  <div class="foot-links" style="left:142px"><div>Privacy Policy</div><div>User Agreement</div></div>

  <div class="foot-head" style="left:269px">Contact Information</div>
  <div class="foot-rule" style="left:269px;width:192px"></div>
  <div class="contact-info">
    <div class="row"><svg width="7" height="10" viewBox="0 0 8 11"><path d="M4 0a4 4 0 014 4c0 3-4 7-4 7S0 7 0 4a4 4 0 014-4z" fill="#fff"/><circle cx="4" cy="4" r="1.5" fill="#3e68b0"/></svg><span>ABN 12045678901 &nbsp;Head Office, 8 Larkfield<br>Drive, Innovation Park, Corrington 4821<br>PO Box 3390 Corrington DC 4821</span></div>
    <div class="row" style="align-items:center"><svg width="6" height="10" viewBox="0 0 6 10"><path d="M4 1C1 2 1 8 4 9" stroke="#fff" stroke-width="1.6" fill="none"/></svg><span class="phone">FREECALL 1800 555 019</span></div>
    <div class="row" style="align-items:center"><svg width="9" height="6" viewBox="0 0 9 6"><rect width="9" height="6" fill="#fff"/><path d="M0 0l4.5 3.5L9 0" stroke="#3e68b0" fill="none"/></svg><span>info@lendyourlessons.com</span></div>
  </div>
  <div class="map" role="img" aria-label="Street map of the head office area"></div>

  <div class="foot-head" style="left:630px">Follow Us</div>
  <div class="foot-rule" style="left:630px;width:126px"></div>
  <div class="social"><div><i></i>Friendbook</div><div><i></i>ProLink</div><div><i></i>Chirper</div><div><i></i>Email</div></div>
</footer>

<div class="copy-bar">
  <span class="left">Copyright@lendyourlessons.com. All Rights Are Reserved.</span>
  <span class="right">Join Us &nbsp;- &nbsp;Login to lendyourlessons Online &nbsp;- &nbsp;Support</span>
</div>
</body>
</html>
```